Surgical Practice specializing in Hand and Upper Extremity Surgery. Dr. Farrow is also a plastic and reconstructive surgeon. These cards will be distributed to referring providers and to patients (e.g. at ER visit for followup). The cards should communicate the highly specialized care we give (as opposed to orthopedic mills which are our competition) and Dr. Farrow's strong credentials and experience. We need a map and clear directions on the back stating location of practice. Our office address is 47 Marlow Crossing, Suite 305, Woburn, MA 01899

Industry/Entity Type

Plastic

```html
<!DOCTYPE html>
<html lang="en">
<head>
<meta charset="utf-8">
<title>Calloway Surgical – Cards</title>
<link href="https://fonts.googleapis.com/css2?family=Arimo:wght@400;700&family=Tinos:wght@400;700&display=swap" rel="stylesheet">
<style>
:root{
  --brand-blue:#3f4d9e;
  --brand-navy:#2f3b8f;
  --ink:#111;
  --paper:#fff;
  --stage:#e9e6e1;
  --rule:#c9cbd6;
}
*{box-sizing:border-box;margin:0;padding:0}
html,body{width:1200px;height:1000px;overflow:hidden}
body{background:var(--stage);font-family:"Arimo",Arial,sans-serif;position:relative}
.card{position:absolute;background:var(--paper);overflow:hidden}
.card--front{left:10px;top:5px;width:800px;height:500px;z-index:2}
.card--back{left:386px;top:494px;width:800px;height:501px;z-index:1}

.brand-box{position:absolute;border:1px solid var(--rule);background:var(--paper);display:flex}
.brand-box__text{flex:1;padding:6px 12px 0;border-right:1px solid var(--rule)}
.brand-box__name{font-weight:700;color:var(--brand-navy);font-size:20px;line-height:1.1;padding-bottom:4px;border-bottom:1.5px solid var(--brand-navy)}
.brand-box__doctor{font-family:"Tinos",serif;font-size:15px;margin-top:5px}
.brand-box__tagline{font-family:"Tinos",serif;font-size:7px;margin-top:7px;white-space:nowrap}
.brand-box__mark{width:84px;display:flex;align-items:center;justify-content:center}
.brand-box__mark--wide{width:102px}
.brand-box__dot{width:26px;height:26px;border-radius:50%;background:var(--brand-navy)}

.card--front .brand-box{left:0;top:0;width:302px;height:72px}
.header-band{position:absolute;left:0;top:0}
.header-title{position:absolute;left:0;top:0;width:800px;height:74px;font-weight:700;white-space:nowrap}
.header-title__lead{position:absolute;left:647px;top:1px;transform:translateX(-50%) scaleX(1.12);color:var(--paper);font-size:26px;line-height:1}
.header-title__main{position:absolute;left:627px;top:28px;transform:translateX(-50%) scaleX(1.2);color:var(--ink);font-size:22px;line-height:20px;text-align:center}

.photo{position:absolute;left:2px;top:78px;width:400px;height:346px;
  background:linear-gradient(160deg,#a48a55 0%,#8fb1d3 45%,#6d9ac9 100%)}

.credentials{position:absolute;left:408px;top:77px;width:392px;height:348px;background:var(--brand-blue);color:var(--paper);padding:6px 0 0 3px;font-weight:700}
.credentials__title{text-align:center;font-size:17px;text-decoration:underline;line-height:19px}
.credentials__heading{font-size:22px;text-decoration:underline;margin-top:8px;line-height:24px}
.credentials__heading--small{font-size:19px;margin-top:4px;line-height:22px}
.row{display:flex;justify-content:space-between;font-size:15px;line-height:19px}
.row--center{justify-content:center}
.edu{padding-left:6px}
.training{margin-top:8px;padding-left:4px}
.training .row{padding-right:10px}

.footer-band{position:absolute;left:0;top:427px}
.work{position:absolute;left:0;top:430px;width:480px;color:var(--paper)}
.work__heading{font-weight:700;font-size:26px;text-decoration:underline;margin-left:52px;line-height:1;letter-spacing:.3px}
.work__text{font-size:13px;line-height:11px;font-weight:700;margin:5px 0 0 5px;width:345px}
.cta{position:absolute;left:490px;top:430px;width:290px;text-align:center;font-weight:700}
.cta__lead{font-size:30px;line-height:32px;color:var(--ink)}
.cta__phone{font-size:38px;line-height:38px;color:var(--brand-navy)}

.card--back .brand-box{left:19px;top:16px;width:368px;height:72px}
.address{position:absolute;left:0;top:108px;width:396px;text-align:center;font-weight:700}
.address__label{font-size:15.5px;line-height:18px}
.address__line{font-size:15px;line-height:18px;color:var(--brand-navy);margin-top:3px}
.map{position:absolute;left:19px;top:161px;width:368px;height:320px;
  background:linear-gradient(180deg,#f7f7f7,#e3e3e3)}
</style>
</head>
<body>

<section class="card card--front">
  <svg class="header-band" width="800" height="77" viewBox="0 0 800 77" aria-hidden="true">
    <polygon points="498,0 800,0 800,72 305,72" fill="var(--brand-blue)"/>
    <line x1="0" y1="74" x2="800" y2="74" stroke="var(--brand-blue)" stroke-width="3"/>
  </svg>
  <div class="brand-box">
    <div class="brand-box__text">
      <div class="brand-box__name">Calloway Surgical</div>
      <div class="brand-box__doctor">Eleanor Farrow, MD</div>
      <div class="brand-box__tagline">Hand and Upper Extremity Surgery | Plastic and Reconstructive Surgery</div>
    </div>
    <div class="brand-box__mark"><span class="brand-box__dot"></span></div>
  </div>
  <div class="header-title">
    <div class="header-title__lead">Specialized Care of</div>
    <div class="header-title__main">Hand and Upper Extremity<br>Surgery</div>
  </div>

  <div class="photo" role="img" aria-label="Photo of the surgeon in scrubs, cap, mask and loupes at work in the operating room"></div>

  <div class="credentials">
    <div class="credentials__title">Dr. Farrow's Experience in Hand and Upper<br>Extremity Surgery</div>
    <div class="credentials__heading">Education:</div>
    <div class="edu">
      <div class="row"><span>Halbrook Medical School MD</span><span>1996</span></div>
      <div class="row row--center"><span>Castlemere Reserve University</span></div>
      <div class="row"><span>B.S., Biochemistry, summa cum laude</span><span>1992</span></div>
      <div class="row"><span>B.A., French, summa cum laude</span><span>1992</span></div>
      <div class="row"><span>Linden High School, Linden Village, Ohio</span><span>1988</span></div>
    </div>
    <div class="credentials__heading credentials__heading--small">PROFESSIONAL TRAINING:</div>
    <div class="training">
      <div class="row"><span>Hand Surgery Fellow, Harbor</span></div>
      <div class="row"><span>Memorial Hospital , Richmond</span><span>2002-2003</span></div>
      <div class="row"><span>Resident, Halbrook Combined</span></div>
      <div class="row"><span>Plastic Surgery Program, Hartford</span><span>1999-2002</span></div>
      <div class="row"><span>Resident, BVMC General Surgery</span></div>
      <div class="row"><span>Program , Hartford</span><span>1996-1999</span></div>
    </div>
  </div>

  <svg class="footer-band" width="800" height="73" viewBox="0 0 800 73" aria-hidden="true">
    <line x1="0" y1="1" x2="800" y2="1" stroke="var(--brand-blue)" stroke-width="2"/>
    <polygon points="0,3 482,3 345,73 0,73" fill="var(--brand-blue)"/>
    <line x1="360" y1="73" x2="496" y2="3" stroke="var(--brand-blue)" stroke-width="2"/>
  </svg>
  <div class="work">
    <div class="work__heading">WORK HISTORY</div>
    <p class="work__text">Private hand surgical practice, working full time as a clinician since 2003,Consultant reviewer for the Journal of Upper Limb SurgeryPeer reviewer for Crane Row</p>
  </div>
  <div class="cta">
    <div class="cta__lead">Call Us Today!</div>
    <div class="cta__phone">(781)555-0148</div>
  </div>
</section>

<section class="card card--back">
  <div class="brand-box">
    <div class="brand-box__text">
      <div class="brand-box__name">Calloway Surgical</div>
      <div class="brand-box__doctor">Eleanor Farrow, MD</div>
      <div class="brand-box__tagline">Hand and Upper Extremity Surgery | Plastic and Reconstructive Surgery</div>
    </div>
    <div class="brand-box__mark brand-box__mark--wide"><span class="brand-box__dot"></span></div>
  </div>
  <div class="address">
    <div class="address__label">Our Office Address</div>
    <div class="address__line">47 Marlow Crossing, Suite 305, Woburn, MA 01899</div>
  </div>
  <div class="map" role="img" aria-label="Site plan map of the office park showing the building, parking, road and sign locations"></div>
</section>

</body>
</html>
```